Martin Hale PA Card Logo

Current logo attached. Its 25 year old logo I have used. Looking for a new fresh elegant professional look/design for a law firm that has high net worth clientele and is estate planning business law firm. Firm mis in Palm Beach Florida.
One sided card linen stock white will be used. Logo section name section. Logo should include nice elegant design using the letter "M" perhapa (I am not wed to current font of the M on current logo.) Be creative there with logo design. My initials are MH.......color scheme I figure 3 tone... Raised Gold Foil, Blue name of firm = Martin Hale, P.A. My practice focus is Family and Business Asset Protection. My name is Martin M. Hale, Esq. Practice specialties include Asset Protection trusts, Business Succession Planning, LLC law, Estate Planning, Medicaid Planning (Maybe put those topics in bullets in a section of card. Bottom of card can be reserved smaller print address phone website and email address. Address section is not as important as logo and topics of practice on front. I foresee address section can be in dark blue. MY name and Topics dark blue as well.
Target Market(s)
affluent; business owners executives; wealth 2-10 million net worth
Industry/Entity Type
business law and estate planning
Contact Information for Business Card
White thick linen one sided

```html
<!DOCTYPE html>
<html lang="en">
<head>
<meta charset="utf-8">
<title>Martin Hale, P.A. — Business Card</title>
<link href="https://fonts.googleapis.com/css2?family=Cinzel:wght@400&family=Quattrocento:wght@400&display=swap" rel="stylesheet">
<style>
  :root {
    --backdrop: #979797;
    --card: #ffffff;
    --navy: #17375a;
    --gold: #d38c1f;
    --slate: #7b7b7b;
  }
  html, body {
    margin: 0;
    padding: 0;
    width: 1200px;
    height: 1000px;
    overflow: hidden;
    background: var(--backdrop);
  }
  .card {
    position: absolute;
    left: 278px;
    top: 314px;
    width: 646px;
    height: 371px;
    background: var(--card);
    overflow: hidden;
  }
  .firm-name {
    position: absolute;
    left: 50px;
    top: 44px;
    margin: 0;
    font-family: "Cinzel", serif;
    font-weight: 400;
    font-size: 28px;
    line-height: 1;
    color: var(--navy);
  }
  .firm-title {
    position: absolute;
    left: 50px;
    top: 89px;
    margin: 0;
    font-family: "Quattrocento", serif;
    font-size: 16px;
    letter-spacing: 2.4px;
    line-height: 1;
    color: var(--navy);
  }
  .practice-areas {
    position: absolute;
    left: 50px;
    top: 134px;
    margin: 0;
    padding: 0;
    list-style: none;
    font-family: "Quattrocento", serif;
    font-size: 20px;
    line-height: 28px;
    color: var(--slate);
  }
  .divider {
    position: absolute;
    left: 50px;
    top: 254px;
    width: 113px;
    height: 1px;
    background: var(--gold);
  }
  .contact {
    position: absolute;
    left: 50px;
    top: 272px;
    margin: 0;
    font-family: "Quattrocento", serif;
    font-style: normal;
    font-size: 15px;
    line-height: 21px;
    color: var(--navy);
  }
  .contact span { display: block; }
  .brand-mark {
    position: absolute;
    left: 385px;
    top: 160px;
    width: 240px;
    text-align: center;
    font-family: "Cinzel", serif;
    font-weight: 400;
    font-size: 34px;
    line-height: 1;
    color: var(--gold);
  }
</style>
</head>
<body>
  <section class="card">
    <h1 class="firm-name">Martin Hale, P.A.</h1>
    <p class="firm-title">ELDER LAW ATTORNEY</p>
    <ul class="practice-areas">
      <li>Asset Protection trusts</li>
      <li>Business Succession Planning</li>
      <li>LLC law · Estate Planning</li>
      <li>Medicaid Planning</li>
    </ul>
    <div class="divider"></div>
    <address class="contact">
      <span>561-555-0148</span>
      <span>hale@palmelderlaw.com</span>
      <span>www.palmelderlaw.com</span>
    </address>
    <div class="brand-mark">Martin Hale</div>
  </section>
</body>
</html>
```